Laser Tattoo Removal Business Cards

We are looking for a professional business card design for a laser tattoo removal business. Ideally looking for a black business card design. The name of the business is Lumen Ink Clearing. We place our cards at local tattoo shops so we ideally are looking for something trendy/edgy to draw both male and female clientele in.

Target Market(s)

Male/Female ages 18-60

Contact Information for Business Card

black background ideally.. hoping to stay within greys, whites and black

Font styles to use
Serif
Sans Serif

Colors
121212
a9a9a9
5c5c5c
f5f5f5
ffffff
7f7f7f
606060
848484
9d9d9d

Requirements
Must have
• Employee Info:
• Marisol Dunmore
• Chief Executive Offer
• m: 919.555.0143
• w: 919.555.0178
• f: 919.555.0192
• mdunmore@lumeninkclearing.com
• Address:
• 4185 Fenwick Pkwy, Suite 210
• Brookhaven, NC 27599
• Website:
• www.lumeninkclearing.com
Nice to have
• Myabe business name on back or logo on back and employee info on the front

```html
<!DOCTYPE html>
<html lang="en">
<head>
<meta charset="utf-8">
<title>Lumen Ink Clearing — Business Card</title>
<link rel="stylesheet" href="https://fonts.googleapis.com/css2?family=Josefin+Sans:wght@400&family=Roboto:wght@400&display=swap">
<style>
  :root {
    --ink: #121212;
    --ink-soft: #1e1e1e;
    --stage: #d4d4d4;
    --white: #ffffff;
    --paper: #f5f5f5;
    --silver-light: #e6e6e6;
    --silver: #c4c4c4;
    --silver-dark: #9d9d9d;
    --grey: #a9a9a9;
    --grey-mid: #7f7f7f;
    --grey-deep: #5c5c5c;
    --champagne: #d8ccb4;
  }
  * { margin: 0; padding: 0; box-sizing: border-box; }
  html, body {
    width: 1200px;
    height: 969px;
    overflow: hidden;
    background: var(--stage);
  }
  .card {
    position: absolute;
    left: 100px;
    top: 199px;
    width: 1000px;
    height: 571px;
    background: var(--ink);
    overflow: hidden;
    box-shadow: 0 18px 40px rgba(0,0,0,0.25);
    font-family: "Roboto", Arial, sans-serif;
  }
  .card__face {
    position: absolute;
    left: 0; top: 0;
    width: 1000px;
    height: 358px;
    background:
      linear-gradient(115deg, rgba(255,255,255,0) 30%, rgba(255,255,255,0.10) 45%, rgba(255,255,255,0) 60%),
      linear-gradient(180deg, var(--ink-soft), var(--ink));
  }
  .card__band {
    position: absolute;
    left: 0; top: 358px;
    width: 1000px;
    height: 179px;
    background:
      linear-gradient(100deg, var(--silver) 0%, var(--paper) 30%, var(--silver-light) 55%, var(--silver) 80%, var(--silver-light) 100%);
  }
  .card__foot {
    position: absolute;
    left: 0; top: 537px;
    width: 1000px;
    height: 34px;
    background: var(--ink);
  }
  .brand {
    position: absolute;
    left: 65px;
    top: 138px;
    width: 380px;
    text-align: center;
    font-family: "Josefin Sans", Arial, sans-serif;
    font-weight: 400;
    color: var(--paper);
    font-size: 48px;
    line-height: 66px;
    letter-spacing: 4px;
    text-transform: uppercase;
  }
  .person {
    position: absolute;
    right: 62px;
    top: 150px;
    text-align: right;
  }
  .person__name {
    color: var(--champagne);
    font-size: 32px;
    letter-spacing: 1px;
    text-transform: uppercase;
    line-height: 38px;
  }
  .person__title {
    color: var(--grey);
    font-size: 24px;
    letter-spacing: 0.5px;
    line-height: 30px;
  }
  .phones {
    position: absolute;
    left: 76px;
    top: 402px;
    list-style: none;
    color: var(--ink);
    font-size: 24px;
    line-height: 31px;
  }
  .details {
    position: absolute;
    right: 62px;
    top: 381px;
    text-align: right;
    color: var(--ink);
    font-size: 24px;
    line-height: 28px;
    font-style: normal;
  }
  .details__web { margin-top: 13px; }
</style>
</head>
<body>
  <div class="card">
    <div class="card__face"></div>
    <div class="card__band"></div>
    <div class="card__foot"></div>

    <div class="brand">Lumen Ink<br>Clearing</div>

    <div class="person">
      <div class="person__name">Marisol Dunmore</div>
      <div class="person__title">Chief Executive Offer</div>
    </div>

    <ul class="phones">
      <li>P) 919.555.0178</li>
      <li>C) 919.555.0143</li>
      <li>F) 919.555.0192</li>
    </ul>

    <address class="details">
      <div>4185 Fenwick Pkwy, Suite 210</div>
      <div>Brookhaven, NC 27599</div>
      <div class="details__web">mdunmore@lumeninkclearing.com</div>
      <div>www.lumeninkclearing.com</div>
    </address>
  </div>
</body>
</html>
```